Resident Guide for Senior Living Community

I need to create an informational magazine for residents that live in an Assisted Living community. This magazine is designed to educate the resident about the different service options and features that the community provides. I don't want to use any of the pictures in the Word Document - please use the uploaded picture instead. The final design should be both informational and elegant. The text in the word document is the actual text that needs to be used in the Resident Guide. Thanks!

Target Market(s)

Senior citizens and adult children (55 - 65 years old)

Industry/Entity Type

Assisted Living

Requirements
Must have
• Must be elegant - think Vellmore Orsay. Needs to have a lot of pictures and the logo must be used. The logo is the Plaque that says The Pellow Court.
Nice to have
• The Word doucment is the old Resident Guide - we are looking for a refresh using the same content.
Should not have
• please do not use any pictures from the Word Document other than the Logo.

```html
<!DOCTYPE html>
<html lang="en">
<head>
<meta charset="utf-8">
<title>The Pellow Court – Resident Guide</title>
<link href="https://fonts.googleapis.com/css2?family=Pinyon+Script&family=Ubuntu:ital,wght@0,400;0,500;0,700;1,500&display=swap" rel="stylesheet">
<style>
  :root{
    --backdrop:#b9b9b9;
    --paper:#ffffff;
    --ink:#1e1e1e;
    --wine:#a3343f;
    --lime:#8cc63f;
    --sky:#0a9bd7;
    --photo-warm:#c9a77f;
  }
  *{box-sizing:border-box;margin:0;padding:0}
  html,body{width:1200px;height:1200px;overflow:hidden;background:var(--backdrop)}
  body{position:relative;font-family:"Ubuntu",sans-serif;color:var(--ink)}
  .page{position:absolute;width:392px;height:555px;background:var(--paper);overflow:hidden}
  .spread-one .page.left{left:217px;top:34px}
  .spread-one .page.right{left:609px;top:34px}
  .spread-two .page.left{left:217px;top:616px}
  .spread-two .page.right{left:609px;top:616px}
  .page.left{box-shadow:inset -10px 0 14px -10px rgba(0,0,0,.12)}
  .page.right{box-shadow:inset 10px 0 14px -10px rgba(0,0,0,.1)}
  .abs{position:absolute}

  .running-head .bar{position:absolute;top:16px;height:5px;background:var(--wine)}
  .running-head .rule{position:absolute;top:19px;height:1px;background:var(--lime)}
  .running-head .label{position:absolute;top:12px;font-size:7.2px;font-weight:700;letter-spacing:.2px;white-space:nowrap}
  .running-head .label em{font-family:"Pinyon Script",cursive;font-style:normal;font-weight:400;font-size:10px;margin-right:2px}

  .photo{position:absolute}
  .strip{position:absolute;background:var(--lime)}

  .block{position:absolute;background:var(--wine)}
  .script{position:absolute;font-family:"Pinyon Script",cursive;font-size:24px;color:#5a5a5a;line-height:1;white-space:nowrap}
  .heading{position:absolute;font-weight:700;font-size:13.6px;letter-spacing:.2px;white-space:nowrap;line-height:1}

  .column{position:absolute;font-size:6px;line-height:8.1px;text-align:justify;hyphens:auto}
  .column p{margin-bottom:8px}
  .dropcap{float:left;font-size:28px;line-height:24px;color:var(--sky);margin:0 2px -2px 0;font-weight:400}
  .signature{font-style:italic;font-weight:500;font-size:6px;line-height:7.5px;text-align:left}

  .folio{position:absolute;top:533px;font-size:7px;font-weight:700}
  .footer-tab{position:absolute;top:533px;width:102px;height:22px;background:var(--sky);color:#fff;font-size:6.2px;display:flex;align-items:center;justify-content:center;white-space:nowrap}
  .footer-tab b{font-weight:700;margin-right:2px}
</style>
</head>
<body>

<section class="spread-one">
  <article class="page left">
    <header class="running-head">
      <span class="bar" style="left:0;width:37px"></span>
      <span class="label" style="left:43px"><em>Resident</em>INFORMATION</span>
      <span class="rule" style="left:135px;width:53px"></span>
    </header>

    <div class="photo" role="img" aria-label="Founder and spouse posed beside a grand piano and floral arrangement" style="left:38px;top:38px;width:306px;height:211px;background:linear-gradient(135deg,#e8ddd3 0%,#c7a997 45%,#3d3a46 100%)"></div>
    <span class="strip" style="left:344px;top:38px;width:11px;height:211px"></span>

    <span class="block" style="left:0;top:271px;width:31px;height:21px"></span>
    <div class="script" style="left:38px;top:268px">Our Pledge</div>
    <h2 class="heading" style="left:37px;top:302px">TO OUR FAMILIES AND RESIDENTS</h2>
    <span class="block" style="left:274px;top:299px;width:81px;height:19px"></span>

    <div class="column" style="left:37px;top:342px;width:152px">
      <p><span class="dropcap">W</span>e promise to devote our love, strength and understanding daily to bring as much happiness, confidence, self-esteem, security and well being as possible to our family of residents. We understand that the real value of our care giving is not measured by our education and credentials or even by our years of experience. It is rather the amount of heart and giving of ourselves, which we willingly share with our resident family members.</p>
      <p>We pledge to create in our homes an atmosphere of friendship, care and love, realizing that an unexpected hug, a gentle taking of a hand or a whispered compliment can do more good and bring more joy than we can imagine.</p>
      <p>We dedicate and commit ourselves to offering a quality of care and service to our residents, which will only be second to the family’s or special friend’s love and concern.</p>
    </div>
    <div class="column" style="left:203px;top:342px;width:152px">
      <p>With the help of a devoted, loving and dedicated management and staff; the family’s and special friend’s interest and love; and with the protection and guidance of God, we make this pledge to each resident and to his/her family and friends.</p>
      <p class="signature" style="margin-top:30px">Composed for the opening of<br>The Pellow Court Alder Springs in 1988</p>
    </div>

    <span class="folio" style="left:34px;top:532px">2</span>
    <div class="footer-tab" style="left:145px"><b>THE PELLOW COURT</b> - SINCE 1988</div>
  </article>

  <article class="page right">
    <header class="running-head">
      <span class="rule" style="left:203px;width:55px"></span>
      <span class="label" style="left:263px"><em>Resident</em>INFORMATION</span>
      <span class="bar" style="left:355px;width:37px"></span>
    </header>

    <span class="block" style="left:0;top:58px;width:34px;height:19px"></span>
    <div class="script" style="left:41px;top:55px">Dear Friends,</div>
    <h2 class="heading" style="left:43px;top:86px">FAMILIES AND OUR SPECIAL RESIDENTS</h2>
    <span class="block" style="left:323px;top:81px;width:32px;height:20px"></span>

    <div class="column" style="left:38px;top:122px;width:151px">
      <p><span class="dropcap">T</span>he Pellow Court is the fulfillment of a dream to honor the life’s work of my father, and a determination to provide a superior level of care, dignity and lifestyle unique in the rapidly expanding field of residential health care. Forty years ago, my mother and I tried to find the kind of care and service The Pellow Court offers for my Alzheimer’s stricken father, but couldn’t. It’s a good feeling knowing we have made a real positive difference in the lives of hundreds of our residents and their families since we opened in 1988. We are here for one reason - to serve you and your family.</p>
      <p>We are different from most other Licensed Assisted Living (as differentiated from lower care level “personal care” facilities) homes in that, most importantly, we are a true Residential Healthcare Home specializing in quality health services, a health care model, and secondarily, a social model. This distinction is crucial because, as your loved one ages, we have the trained, competent and essential staff members to handle their increasing health and personal health needs. Of course,</p>
    </div>
    <div class="column" style="left:203px;top:122px;width:151px">
      <p>we provide all the entertainment and stimulating activities, exercise programs, mental stimulation, etc; but from Day One of this family business, we have focused on providing top- level health care services first and foremost, complemented by our solid social/activity/hospitality schedule. Most other residential care facilities put their social program first and are primarily a social model giving less than full attention, and importance (and financial support) to quality personal wellness and health care services. As you might expect, the health care model is much more expensive to implement and operate.</p>
      <p>Additionally, a true advantage The Pellow Court has over others is our bundled services program for one competitive, flat fee (with the exception of a few electives, such as personal telephone, special therapy and beauty appointments). Our rates are all-inclusive; therefore, our families appreciate the fact that there are no surprise add-ons each month. Our one fee covers every need your family member has as often as he or she needs it.</p>
    </div>

    <span class="strip" style="left:38px;top:318px;width:11px;height:200px"></span>
    <div class="photo" role="img" aria-label="Entrance sign of the community with flower beds and the main building behind" style="left:49px;top:318px;width:306px;height:200px;background:linear-gradient(180deg,#a9c8e6 0%,#dfe8ee 35%,#6f8a4c 62%,#3f6a2c 100%)"></div>

    <span class="folio" style="left:357px;top:532px">3</span>
    <div class="footer-tab" style="left:146px"><b>THE PELLOW COURT</b> - SINCE 1988</div>
  </article>
</section>

<section class="spread-two">
  <article class="page left">
    <header class="running-head">
      <span class="bar" style="left:0;width:37px"></span>
      <span class="label" style="left:43px"><em>Resident</em>INFORMATION</span>
      <span class="rule" style="left:135px;width:53px"></span>
    </header>

    <div class="column" style="left:37px;top:58px;width:152px">
      <p>From personal laundry, numerous daily diaper changes, complete feeding assistance at meals, multiple nursing visits per day, to daily suite, and bathroom cleaning - whatever is needed and appropriate is promptly performed without extra add-on charges.</p>
      <p>You’ll be interested in knowing our extraordinary Care Staff to Resident ratio average of 1:3/1:5 is incomparable, and largely accounts for our capability of managing higher care residents as their needs increase, making it highly unlikely your family member will ever have to move from The Pellow Court.</p>
      <p>During the past nearly thirty (30) years, our home has established a superior reputation, a tradition of excellence and an outstanding record of managing our</p>
    </div>
    <div class="column" style="left:203px;top:58px;width:152px">
      <p>residents’ day-to-day healthcare needs (i.e. Alzheimer’s, Parkinson’s Disease, and acute memory impaired persons, stroke, heart attack, arthritis, cancer and accident victims, individuals with various chronic and emotional or physical disabilities) offering solutions for an increasing number of families with loved ones who can no longer live independently.</p>
      <p>Further, setting us apart from most other residential health care homes is our ability to care for couples, often with differing levels of independence and healthcare needs. Enabling these couples to continue living together and not be forced into separate living facilities when one has more extensive health care requirements than the other is something we’ve identified since 1989, as a real needed service and accommodation.</p>
    </div>

    <div class="photo" role="img" aria-label="Plated entrée with asparagus on a dining table" style="left:37px;top:199px;width:153px;height:106px;background:linear-gradient(135deg,#efe2c2 0%,#d9c394 100%)"></div>
    <span class="strip" style="left:190px;top:199px;width:12px;height:106px"></span>
    <div class="photo" role="img" aria-label="Lounge with fireplace, sofas and chandeliers" style="left:202px;top:199px;width:153px;height:106px;background:linear-gradient(180deg,#e8d6b8 0%,#9c6d42 100%)"></div>
    <div class="photo" role="img" aria-label="Dining room with wooden beams, chandeliers and set tables" style="left:37px;top:305px;width:318px;height:200px;background:linear-gradient(180deg,#f2e4c6 0%,#c99b62 55%,#7a4a26 100%)"></div>
    <span class="strip" style="left:37px;top:505px;width:318px;height:11px"></span>

    <span class="folio" style="left:34px;top:532px">4</span>
    <div class="footer-tab" style="left:145px"><b>THE PELLOW COURT</b> - SINCE 1988</div>
  </article>

  <article class="page right">
    <header class="running-head">
      <span class="rule" style="left:203px;width:55px"></span>
      <span class="label" style="left:263px"><em>Resident</em>INFORMATION</span>
      <span class="bar" style="left:355px;width:37px"></span>
    </header>

    <span class="strip" style="left:38px;top:58px;width:317px;height:8px"></span>
    <div class="photo" role="img" aria-label="Screened porch with wicker furniture, green cushions and garden view" style="left:38px;top:66px;width:317px;height:186px;background:linear-gradient(135deg,#e9efe0 0%,#8fb25a 45%,#b08a5a 100%)"></div>

    <div class="column" style="left:38px;top:270px;width:151px">
      <p>There are many other features and benefits of The Pellow Court, but these are most prominent: our small size of only 25 suites and penthouses in Alder Springs and 50 suites in Cedar Ridge, our less than 10 % annual staff turnover, our 1:3/1:5 Healthcare Staff to Resident ratio, our central locations, and our legendary 24- hour care giving. My personal promise to each resident and family is that we will strive each day to provide the very best healthcare and personal services humanly possible for our residents who range in age from 65-100+ years.</p>
      <p>We set the standard for our industry, both in Harlow and across the South. We sincerely realize that our responsibility is not only to aspire and continue to be the best, but to improve every day to make living at The Pellow Court the best possible alternative for those unable to continue living in their own homes or at alternative living arrangements. (Especially, if they are unable to provide the level of care you desire and expect, and your family member requires.)</p>
      <p>Thank you for thinking of us. It would be a pleasure to meet you personally.</p>
      <p>Just call 555-014-2280 for an appointment. All best wishes to you and your family,</p>
    </div>
    <p class="column signature" style="left:38px;top:511px;width:151px">Founder and President</p>

    <span class="strip" style="left:203px;top:270px;width:11px;height:246px"></span>
    <div class="photo" role="img" aria-label="Founder and spouse standing in a warmly furnished sitting room" style="left:214px;top:270px;width:178px;height:246px;background:linear-gradient(160deg,#e6d9c9 0%,#b89672 50%,#3a3f52 100%)"></div>

    <span class="folio" style="left:357px;top:532px">5</span>
    <div class="footer-tab" style="left:146px"><b>THE PELLOW COURT</b> - SINCE 1988</div>
  </article>
</section>

</body>
</html>
```